Save the date for wedding

A save the date for our wedding. We're looking for a simple and sleek invite. I would prefer not alot of calligraphy. Minimalism is good. The basic info to include is as follows:
Names: Mona and Felix
Date: June 9th
Where: Ottawa, Ontario
In small print please include that there will be a reception in Edmonton AB September 1st for those who cannot make it to Ottawa.
Please see the attached file for a style idea. Doesn’t have to be exactly like that, but something like that.

```html
<!DOCTYPE html>
<html lang="en">
<head>
<meta charset="utf-8">
<title>Mona &amp; Felix — Save the Date</title>
<link rel="stylesheet" href="https://fonts.googleapis.com/css2?family=Montserrat:wght@400;500&family=Six+Caps&family=Playfair+Display:ital,wght@1,700&family=Open+Sans:wght@400&display=swap">
<style>
  :root {
    --card-bg: #686868;
    --frame: #c4c4c4;
    --ink: #ffffff;
    --gold: #b99a3b;
  }
  * { margin: 0; padding: 0; box-sizing: border-box; }
  html, body { width: 1200px; height: 851px; overflow: hidden; background: var(--card-bg); }
  .card {
    position: relative;
    width: 1200px;
    height: 851px;
    background: var(--card-bg);
    color: var(--ink);
    text-align: center;
  }
  .frame-outer {
    position: absolute;
    inset: 16px;
    border: 5px solid var(--frame);
  }
  .frame-inner {
    position: absolute;
    inset: 28px;
    border: 2px solid var(--frame);
    opacity: 0.7;
  }
  .date {
    position: absolute;
    top: 96px;
    left: 0; right: 0;
    font-family: "Montserrat", sans-serif;
    font-weight: 500;
    font-size: 36px;
    letter-spacing: 5px;
  }
  .names {
    position: absolute;
    top: 172px;
    left: 0; right: 0;
    font-family: "Six Caps", sans-serif;
    font-size: 330px;
    line-height: 330px;
    letter-spacing: 14px;
    white-space: nowrap;
  }
  .ring {
    position: absolute;
    top: 510px;
    left: 562px;
    width: 76px;
    height: 90px;
  }
  .place {
    position: absolute;
    top: 646px;
    left: 0; right: 0;
    font-family: "Playfair Display", serif;
    font-style: italic;
    font-weight: 700;
    font-size: 43px;
    letter-spacing: 3px;
  }
  .reception-note {
    position: absolute;
    top: 748px;
    left: 0; right: 0;
    font-family: "Open Sans", sans-serif;
    font-size: 25px;
  }
</style>
</head>
<body>
  <main class="card">
    <div class="frame-outer"></div>
    <div class="frame-inner"></div>

    <p class="date">JUNE 9, 2018</p>
    <h1 class="names">MONA &amp; FELIX</h1>

    <svg class="ring" viewBox="0 0 76 90" aria-hidden="true">
      <circle cx="38" cy="56" r="27" fill="none" stroke="var(--gold)" stroke-width="8"/>
      <polygon points="24,12 31,4 45,4 52,12 38,28" fill="var(--ink)"/>
    </svg>

    <p class="place">Ottawa, Ontario</p>
    <p class="reception-note">Reception in Edmonton AB September 1st for those who cannot make it to Ottawa.</p>
  </main>
</body>
</html>
```